Business Card Design

Quorvel Software Limited develops and sells venue and event management software called Quorvel Stagehand, which is available in the cloud or on-premise. The company was established in 1986. Most of our customers are performing arts venues, museums and festivals. Our existing design is a bit dull. We need to convey that we are both innovative and reliable.
Not all our people show their mobile phone numbers on their cards, so the design needs to work land line and mobile or land line only.

Industry/Entity Type

Software

Contact Information for Business Card

Helen Trasko
Director
Quorvel Software Limited
42B Milbrook Lane, Epsom, Surrey, KT19 4DN
Telephone: +44 (0)1372 640913
Mobile: +44 (0)7945 216804
Email: htrasko@quorvel.net
Web: www.quorvel.net

```html
<!DOCTYPE html>
<html lang="en">
<head>
<meta charset="utf-8">
<title>Quorvel Software Limited – Business Card</title>
<link href="https://fonts.googleapis.com/css2?family=Open+Sans:ital,wght@0,400;0,600;0,700;0,800;1,400&display=swap" rel="stylesheet">
<style>
  :root {
    --backdrop: #a9aaae;
    --paper: #ffffff;
    --navy: #1f5a80;
    --navy-deep: #184a6b;
    --ocean: #2f7fb0;
    --sky: #8fc0e0;
    --ink: #1e4f74;
    --muted: #4a5a68;
  }
  * { box-sizing: border-box; margin: 0; padding: 0; }
  html, body { width: 1200px; height: 863px; overflow: hidden; }
  body {
    background: var(--backdrop);
    font-family: "Open Sans", Arial, sans-serif;
    position: relative;
  }
  .card {
    position: absolute;
    left: 300px;
    width: 600px;
    height: 340px;
    border-radius: 22px;
    overflow: hidden;
    background: var(--paper);
    box-shadow: 0 10px 28px rgba(0,0,0,.22);
  }
  .card--front { top: 70px; }
  .card--back  { top: 455px; }

  /* Front card */
  .brand { position: absolute; left: 44px; top: 128px; }
  .brand__row { display: flex; align-items: center; gap: 10px; }
  .brand__mark { width: 26px; height: 26px; background: var(--navy); }
  .brand__name {
    font-weight: 800; font-size: 30px; letter-spacing: 1px; color: var(--ink); line-height: 1;
  }
  .brand__tagline {
    margin-top: 6px; font-size: 13px; color: var(--muted);
  }

  /* Back card */
  .back__shape { position: absolute; inset: 0; width: 600px; height: 340px; }
  .back__brand { position: absolute; left: 40px; top: 70px; }
  .back__brand .brand__name { font-size: 38px; }
  .back__brand .brand__mark { width: 32px; height: 32px; }
  .back__web { margin-top: 6px; font-size: 13px; color: var(--muted); }

  .contact { position: absolute; left: 330px; top: 84px; color: #fff; }
  .contact__name { font-size: 24px; font-weight: 700; line-height: 1.1; }
  .contact__role { font-size: 13px; color: var(--sky); margin-bottom: 14px; }
  .contact__address { font-size: 13px; line-height: 1.35; margin-bottom: 14px; }
  .contact__list { list-style: none; font-size: 13px; line-height: 1.55; }
  .contact__list li { display: flex; align-items: center; gap: 8px; }
  .contact__icon { width: 12px; height: 12px; flex: none; }
</style>
</head>
<body>

  <section class="card card--front" aria-label="Business card front">
    <div class="brand">
      <div class="brand__row">
        <span class="brand__mark"></span>
        <span class="brand__name">QUORVEL</span>
      </div>
      <p class="brand__tagline">venue and Event management software</p>
    </div>
  </section>

  <section class="card card--back" aria-label="Business card back">
    <svg class="back__shape" viewBox="0 0 600 340" aria-hidden="true">
      <defs>
        <linearGradient id="panelFill" x1="0" y1="0" x2="1" y2="1">
          <stop offset="0" stop-color="#2a6690"/>
          <stop offset="1" stop-color="#184a6b"/>
        </linearGradient>
      </defs>
      <path d="M300 0 C 270 120, 190 250, 0 300 L0 340 L600 340 L600 0 Z" fill="var(--ocean)"/>
      <path d="M322 0 C 292 130, 212 262, 0 318 L0 340 L600 340 L600 0 Z" fill="url(#panelFill)"/>
    </svg>

    <div class="back__brand">
      <div class="brand__row">
        <span class="brand__mark"></span>
        <span class="brand__name">QUORVEL</span>
      </div>
      <p class="back__web">www.quorvel.net</p>
    </div>

    <div class="contact">
      <p class="contact__name">Helen Trasko</p>
      <p class="contact__role">Director</p>
      <p class="contact__address">Quorvel Software Limited<br>42B Milbrook Lane, Epsom, Surrey,<br>KT19 4DN</p>
      <ul class="contact__list">
        <li>
          <svg class="contact__icon" viewBox="0 0 12 12" aria-label="Mobile"><rect x="3" y="0.5" width="6" height="11" rx="1" fill="none" stroke="#8fc0e0"/><circle cx="6" cy="9.5" r="0.7" fill="#8fc0e0"/></svg>
          +44 (0)7945 216804
        </li>
        <li>
          <svg class="contact__icon" viewBox="0 0 12 12" aria-label="Telephone"><path d="M2 1.5 L4.5 1 L5.5 4 L4 5 C4.8 6.8 5.2 7.2 7 8 L8 6.5 L11 7.5 L10.5 10 C6 10.5 1.5 6 2 1.5 Z" fill="none" stroke="#8fc0e0"/></svg>
          +44 (0)1372 640913
        </li>
        <li>
          <svg class="contact__icon" viewBox="0 0 12 12" aria-label="Email"><rect x="0.5" y="2.5" width="11" height="7" fill="none" stroke="#8fc0e0"/><path d="M0.5 2.5 L6 7 L11.5 2.5" fill="none" stroke="#8fc0e0"/></svg>
          htrasko@quorvel.net
        </li>
      </ul>
    </div>
  </section>

</body>
</html>
```